Candle company needs a label for candle

Looking for a designer to create my candle label. I am going to attach a few pictures of my vision for the label as well as my Company Logo and jar I have puchased. I'm going for the modern rustic feel but you are the designer and have full trust in your abilities. The label is going to be printed on Kraft paper (2x3) so looking for the font to be black. The candle label MUST include the following information:
Candle Birchway Co.
NO. 01: Eucalyptus + Spearmint
Handmade In NJ
Soy Wax
9oz

Industry/Entity Type

Candle Industry

Colors

Designer to choose colors to be used in the design.

Requirements
Should not have
• Any images

```html
<!DOCTYPE html>
<html lang="en">
<head>
<meta charset="utf-8">
<title>Candle Birchway Co. — Label Variants</title>
<link href="https://fonts.googleapis.com/css2?family=Alegreya:wght@400;700&display=swap" rel="stylesheet">
<style>
  :root {
    --page-bg: #ffffff;
    --kraft-dark: #7d6128;
    --kraft-mid: #9a7d43;
    --kraft-light: #b7a175;
    --kraft-ink: #ffffff;
    --band-dark: #1f1a19;
    --band-mid: #3a3230;
    --rose-edge: #6e5d56;
    --rose-ink: #3b302d;
  }
  * { margin: 0; padding: 0; box-sizing: border-box; }
  html, body { width: 1200px; height: 803px; overflow: hidden; background: var(--page-bg); }
  .canvas { position: relative; width: 1200px; height: 803px; }

  .label {
    position: absolute;
    width: 423px;
    height: 281px;
    font-family: "Alegreya", Georgia, serif;
    font-variant-numeric: lining-nums;
    overflow: hidden;
  }
  .label--kraft {
    left: 103px; top: 309px;
    color: var(--kraft-ink);
    background: radial-gradient(ellipse at 50% 45%, var(--kraft-light) 0%, var(--kraft-mid) 45%, var(--kraft-dark) 100%);
    --rule: rgba(255,255,255,0.75);
  }
  .label--rose {
    left: 667px; top: 302px;
    color: var(--rose-ink);
    background: linear-gradient(180deg, var(--band-dark) 0%, var(--band-mid) 50%, var(--band-dark) 100%);
    --rule: rgba(59,48,45,0.7);
  }
  .label__frame { position: absolute; inset: 0; width: 100%; height: 100%; }

  .label__text { position: absolute; left: 0; width: 100%; text-align: center; white-space: nowrap; line-height: 1; }

  .brand-name { font-weight: 400; font-size: 24px; letter-spacing: 0.3px; }
  .scent-name { font-size: 15px; letter-spacing: 1.6px; }
  .scent-name .scent-number { font-size: 19px; letter-spacing: 1px; }
  .origin { font-weight: 700; font-size: 10px; letter-spacing: 1.6px; }

  .rule {
    position: absolute;
    left: 130px; width: 162px; height: 0;
    border-top: 1px dotted var(--rule);
  }

  .spec { position: absolute; font-weight: 700; white-space: nowrap; line-height: 1; }
  .spec--wax { font-size: 16px; letter-spacing: 2px; }
  .spec--size { font-size: 19px; }
  .spec--size small { font-size: 13px; font-weight: 400; letter-spacing: 1px; }
  .spec-dot {
    position: absolute; width: 5px; height: 5px; border-radius: 50%;
    background: currentColor; left: 208px;
  }
</style>
</head>
<body>
<main class="canvas">

  <section class="label label--kraft" aria-label="Kraft label variant">
    <svg class="label__frame" viewBox="0 0 423 281" aria-hidden="true">
      <path d="M40 25 H380 A18 18 0 0 0 398 43 V240 A18 18 0 0 0 380 258 H40 A18 18 0 0 0 22 240 V43 A18 18 0 0 0 40 25 Z"
            fill="none" stroke="#ffffff" stroke-width="1.2"/>
      <path d="M40 30 H380 A13 13 0 0 0 393 43 V240 A13 13 0 0 0 380 253 H40 A13 13 0 0 0 27 240 V43 A13 13 0 0 0 40 30 Z"
            fill="none" stroke="#ffffff" stroke-width="1"/>
    </svg>
    <p class="label__text brand-name" style="top:84px;">Candle Birchway Co.</p>
    <span class="rule" style="top:153px;"></span>
    <p class="label__text scent-name" style="top:163px;">NO. <span class="scent-number">01</span> : EUCALYPTUS + SPEARMINT</p>
    <p class="label__text origin" style="top:190px;">HANDMADE IN NJ</p>
    <span class="rule" style="top:211px;"></span>
    <p class="spec spec--wax" style="left:60px; top:228px;">SOY WAX</p>
    <span class="spec-dot" style="top:233px;"></span>
    <p class="spec spec--size" style="left:331px; top:226px;">9 <small>OZ</small></p>
  </section>

  <section class="label label--rose" aria-label="Dark band label variant">
    <svg class="label__frame" viewBox="0 0 423 281" aria-hidden="true">
      <defs>
        <linearGradient id="rosePanel" x1="0" y1="0" x2="1" y2="0">
          <stop offset="0" stop-color="#d7b39e"/>
          <stop offset="0.45" stop-color="#f1dbcd"/>
          <stop offset="1" stop-color="#dcb9a4"/>
        </linearGradient>
      </defs>
      <path d="M50 30 H371 A18 18 0 0 0 389 48 V233 A18 18 0 0 0 371 251 H50 A18 18 0 0 0 32 233 V48 A18 18 0 0 0 50 30 Z"
            fill="url(#rosePanel)" stroke="var(--rose-edge)" stroke-width="1.5"/>
      <path d="M50 35 H371 A13 13 0 0 0 384 48 V233 A13 13 0 0 0 371 246 H50 A13 13 0 0 0 37 233 V48 A13 13 0 0 0 50 35 Z"
            fill="none" stroke="var(--rose-edge)" stroke-width="1"/>
    </svg>
    <p class="label__text brand-name" style="top:84px;">Candle Birchway Co.</p>
    <span class="rule" style="top:151px;"></span>
    <p class="label__text scent-name" style="top:160px;">NO. <span class="scent-number">01</span> : EUCALYPTUS + SPEARMINT</p>
    <p class="label__text origin" style="top:186px;">HANDMADE IN NJ</p>
    <span class="rule" style="top:206px;"></span>
    <p class="spec spec--wax" style="left:67px; top:222px;">SOY WAX</p>
    <span class="spec-dot" style="top:227px;"></span>
    <p class="spec spec--size" style="left:325px; top:220px;">9 <small>OZ</small></p>
  </section>

</main>
</body>
</html>
```